Flyer for Summer Programs for Youth Interfaith Organization

We need a 6x9" front and back design advertising our summer programs. The flyer should have pictures, descriptions, and space for a mailing label and return address, etc. It should be fun and inviting and be something we can mail out. We are an interfaith organization that does education programs for students of all religious and non-religious backgrounds. Our goals are to bring students together for shared learning, community service, and leadership development.

Target Market(s)

youth and their families

Industry/Entity Type

Education

Font styles to use
Serif

Colors

Designer to choose colors to be used in the design.

Requirements
Must have
• pictures, space for a mailing label and return address

```html
<!DOCTYPE html>
<html lang="en">
<head>
<meta charset="utf-8">
<title>Summer Programs Mailer</title>
<link href="https://fonts.googleapis.com/css2?family=Comfortaa:wght@400;600;700&display=swap" rel="stylesheet">
<style>
  :root {
    --page: #ffffff;
    --navy: #4267a8;
    --sky: #62a3dc;
    --sky-text: #6fb3ef;
    --ink: #3f64a6;
    --white: #ffffff;
    --shadow: #8c8c8c;
    --photo-a: #8f7a5e;
    --photo-b: #7fae5a;
  }
  * { margin: 0; padding: 0; box-sizing: border-box; }
  html, body { width: 1200px; height: 720px; overflow: hidden; background: var(--page); }
  body { position: relative; font-family: "Comfortaa", sans-serif; }

  .card { position: absolute; }
  .card-shadow { position: absolute; background: var(--shadow); }

  /* Address side */
  .address-side { left: 74px; top: 191px; width: 508px; height: 339px; background: var(--navy); }
  .address-panel { position: absolute; left: 9px; top: 10px; width: 243px; height: 319px; background: var(--sky); }
  .return-address { position: absolute; left: 34px; top: 35px; width: 170px; font-size: 14px; line-height: 19px; color: var(--ink); }
  .return-address .gap { display: block; height: 3px; }
  .address-line { position: absolute; left: 33px; width: 170px; border-top: 1px solid var(--white); }
  .mailing-label { position: absolute; left: 33px; top: 181px; width: 168px; height: 112px; border: 1px dotted var(--white);
    display: flex; align-items: center; justify-content: center; text-align: center;
    font-size: 21px; line-height: 29px; font-weight: 600; color: var(--ink); }
  .photo { position: absolute; left: 262px; width: 236px; }
  .photo-group { top: 10px; height: 154px; background: linear-gradient(160deg, var(--photo-a), #9d5544 40%, var(--photo-b) 80%); }
  .photo-scroll { top: 175px; height: 154px; background: linear-gradient(200deg, #a88566, #c9a67b 45%, var(--photo-b) 90%); }

  /* Info side */
  .info-side { left: 619px; top: 190px; width: 508px; height: 340px; background: var(--sky); }
  .info-panel { position: absolute; left: 10px; top: 10px; width: 489px; height: 320px; background: var(--navy); color: var(--white); text-align: center; }
  .headline { position: absolute; top: 18px; width: 100%; font-size: 23px; font-weight: 700; color: var(--sky-text); }
  .intro { position: absolute; left: 18px; top: 56px; width: 453px; font-size: 14px; line-height: 18px; }
  .intro strong { font-weight: 700; }
  .signup { position: absolute; top: 163px; width: 100%; font-size: 14px; }
  .signup .link { color: var(--sky-text); }
  .sessions { position: absolute; left: 25px; top: 192px; width: 440px; display: flex; justify-content: space-between; }
  .session { width: 140px; font-size: 14px; line-height: 18px; }
  .session .venue { color: var(--sky-text); font-weight: 600; }
  .contacts { position: absolute; top: 262px; width: 100%; font-size: 13px; line-height: 18px; }
  .contact { display: flex; justify-content: center; align-items: center; gap: 5px; }
  .contact svg { width: 14px; height: 12px; }
  .social-mark { width: 11px; height: 11px; background: var(--white); border-radius: 2px; display: inline-block; }
</style>
</head>
<body>

  <div class="card-shadow" style="left:82px; top:199px; width:508px; height:339px;"></div>
  <section class="card address-side">
    <div class="address-panel">
      <p class="return-address">From: 418 Harbor View Lane<span class="gap"></span>Maple Grove, CA 90000<span class="gap"></span>To:</p>
      <div class="address-line" style="top:103px; left:58px; width:145px;"></div>
      <div class="address-line" style="top:122px;"></div>
      <div class="address-line" style="top:142px;"></div>
      <div class="address-line" style="top:161px;"></div>
      <div class="mailing-label">Mailing<br>label</div>
    </div>
    <div class="photo photo-group" role="img" aria-label="Photo of students in matching green shirts standing together in front of a brick building"></div>
    <div class="photo photo-scroll" role="img" aria-label="Photo of students gathered around an open scroll on a wooden table during a visit to a house of worship"></div>
  </section>

  <div class="card-shadow" style="left:627px; top:198px; width:508px; height:340px;"></div>
  <section class="card info-side">
    <div class="info-panel">
      <h1 class="headline">Amazing interfaith programms!</h1>
      <p class="intro"><strong>Common Ground Youth Leadership Initiative</strong> – Join students from all over Los Angeles and Orange Counties for community service, leadership development, visiting various houses of worship, and fun! This three day program can earn you a $100 college scholarship!</p>
      <p class="signup">To sign up, visit <span class="link">cgyli.example.org</span></p>
      <div class="sessions">
        <p class="session"><span class="venue">Westfield University –</span> July 17-19</p>
        <p class="session"><span class="venue">Orchard University –</span> July 24-26</p>
        <p class="session"><span class="venue">Bayside State –</span> July 31 - Aug. 2</p>
      </div>
      <div class="contacts">
        <p class="contact"><svg viewBox="0 0 14 12"><circle cx="4.5" cy="4.5" r="3" fill="none" stroke="#fff" stroke-width="2"/><circle cx="9.5" cy="7.5" r="3" fill="none" stroke="#fff" stroke-width="2"/></svg>www.brightpathpartners.org</p>
        <p class="contact"><svg viewBox="0 0 14 12"><rect x="0.5" y="1.5" width="13" height="9" fill="#fff"/><path d="M0.5 1.5 L7 6.5 L13.5 1.5" fill="none" stroke="#4267a8" stroke-width="1.4"/></svg>info@brightpathpartners.org</p>
        <p class="contact"><span class="social-mark"></span>commongroundyouth</p>
      </div>
    </div>
  </section>

</body>
</html>
```